Pat Greene Billboard

**Task Description: Billboard Design for Self Storage Facility**

**Objective:**
Design a captivating billboard to promote our self-storage facility with a focus on our convenient location and online rental capabilities.

**Key Messages to Include:**
1. **Location Emphasis:** Highlight that our facility is located right beside the billboard (maybe by using an arrow pointing left).
2. **Online Rental Convenience:** Feature prominently that customers can "Rent Online Anytime!” or that we are "Always Open Online!"

**Target Audience:**
- Local residents looking for convenient self-storage solutions.
- Businesses needing storage space accessible around the clock.

**Design Elements:**
1. **Visual Impact:** Eye-catching graphics and colors that stand out against the surroundings.
2. **Clear Text:** Bold and concise messaging that can be read and understood quickly.
3. **Contact Information:** Include our phone number and website URL for easy access to further information.

**Additional Information:**
- Billboard dimensions: 12 ft. x 24 ft.
- Preferred color scheme: Bright and attention-grabbing, but professional.
- Branding: Incorporate our logo and brand colors to maintain consistency.

**Deliverables:**
- High-resolution digital file compatible with billboard printing specifications.
- Consider mockups or visualizations for presentation purposes.

Please note that I have attached current logos/graphics that we would love to incorporate into the billboard as well as a picture of our current billboard. Our logo (Pat Greene Self Storage - PG navy.png) MUST be incorporated into the billboard. Also feel free to add any of the current descriptions from the picture of our current billboard into the design. Instead of using "Climate Controlled" use "Temperature Controlled". Thank you for your attention to these details. We look forward to reviewing your proposed design!

```html
<!DOCTYPE html>
<html lang="en">
<head>
<meta charset="utf-8">
<title>Pat Greene Billboard</title>
<link href="https://fonts.googleapis.com/css2?family=Montserrat:wght@700;800;900&display=swap" rel="stylesheet">
<style>
  :root {
    --navy: #00245a;
    --sky: #00aeef;
    --ink: #111111;
    --frame: #2a2a2a;
    --paper: #ffffff;
    --stage: #e9e9e9;
    --door: #b8b199;
    --door-dark: #8c8570;
    --hall: #d9d9d6;
  }
  * { box-sizing: border-box; margin: 0; padding: 0; }
  html, body { width: 1200px; height: 1200px; overflow: hidden; }
  body { background: var(--stage); font-family: "Montserrat", Arial, sans-serif; position: relative; }

  .billboard {
    position: absolute; left: 28px; top: 316px; width: 1152px; height: 576px;
    background: var(--paper); overflow: hidden;
  }
  .brand-panel { position: absolute; left: 0; top: 0; width: 808px; height: 289px; }
  .brand-name {
    position: absolute; left: 0; width: 808px; text-align: center;
    color: var(--navy); font-weight: 800; line-height: 1;
  }
  .brand-name--main { top: 58px; font-size: 92px; letter-spacing: 1px; }
  .brand-name--sub { top: 160px; font-size: 38px; letter-spacing: 22px; padding-left: 22px; }

  .tagline {
    position: absolute; left: 41px; top: 225px; width: 742px; height: 47px;
    border: 2.5px solid var(--frame); border-radius: 6px;
    display: flex; align-items: center; justify-content: center;
    color: #333; font-weight: 800; font-size: 28.5px; letter-spacing: 0.5px; white-space: nowrap;
  }

  .facility-photo {
    position: absolute; left: 808px; top: 0; width: 344px; height: 289px;
    background: linear-gradient(90deg, var(--door) 0%, var(--door-dark) 30%, var(--hall) 48%, var(--hall) 55%, var(--door-dark) 70%, var(--door) 100%);
  }

  .web-band {
    position: absolute; left: 0; top: 289px; width: 1152px; height: 90px;
    background: var(--navy); color: var(--paper);
    display: flex; align-items: center; justify-content: center;
    font-weight: 800; font-size: 64px; letter-spacing: 0.5px; white-space: nowrap;
  }

  .feature { position: absolute; top: 379px; height: 94px; display: flex; align-items: center; }
  .feature--temp { left: 104px; }
  .feature--rent { left: 623px; }
  .feature-icon { width: 82px; height: 82px; margin-right: 20px; flex: none; }
  .feature-text { color: var(--ink); font-weight: 900; font-size: 40px; line-height: 37px; }

  .call-band { position: absolute; left: 0; top: 473px; width: 1152px; height: 103px; }
  .call-band svg { position: absolute; left: 0; top: 0; }
  .phone-number {
    position: absolute; left: 508px; top: 0; height: 103px;
    display: flex; align-items: center;
    color: var(--paper); font-weight: 800; font-size: 90px; letter-spacing: 1px; white-space: nowrap;
  }
</style>
</head>
<body>
  <div class="billboard">
    <div class="brand-panel">
      <div class="brand-name brand-name--main">PAT GREENE</div>
      <div class="brand-name brand-name--sub">SELF STORAGE</div>
      <div class="tagline">SELF STORAGE IN THE HEART OF GEORGIA</div>
    </div>

    <div class="facility-photo" role="img" aria-label="Photo of an indoor storage hallway lined with roll-up unit doors"></div>

    <div class="web-band">www.harborlinestorage.com</div>

    <div class="feature feature--temp">
      <svg class="feature-icon" viewBox="0 0 82 82" aria-hidden="true">
        <circle cx="41" cy="41" r="39" fill="none" stroke="var(--navy)" stroke-width="2"/>
        <circle cx="41" cy="41" r="34" fill="var(--navy)"/>
        <rect x="33" y="20" width="10" height="28" rx="5" fill="none" stroke="#fff" stroke-width="2.5"/>
        <circle cx="38" cy="53" r="7" fill="none" stroke="#fff" stroke-width="2.5"/>
        <line x1="38" y1="30" x2="38" y2="50" stroke="#fff" stroke-width="2.5"/>
        <circle cx="27" cy="25" r="1.3" fill="#fff"/><circle cx="27" cy="31" r="1.3" fill="#fff"/><circle cx="27" cy="37" r="1.3" fill="#fff"/>
        <circle cx="54" cy="45" r="8" fill="none" stroke="#fff" stroke-width="2.5"/>
        <polyline points="50,45 53,48 58,42" fill="none" stroke="#fff" stroke-width="2.5"/>
      </svg>
      <div class="feature-text">TEMPERATURE<br>CONTROLLED</div>
    </div>

    <div class="feature feature--rent">
      <svg class="feature-icon" viewBox="0 0 82 82" aria-hidden="true">
        <circle cx="41" cy="41" r="39" fill="none" stroke="var(--navy)" stroke-width="2"/>
        <circle cx="41" cy="41" r="34" fill="var(--navy)"/>
        <rect x="28" y="40" width="32" height="20" rx="3" fill="#fff"/>
        <circle cx="30" cy="42" r="7" fill="var(--navy)" stroke="#fff" stroke-width="2.5"/>
        <line x1="35" y1="37" x2="55" y2="22" stroke="#fff" stroke-width="4"/>
        <line x1="49" y1="26" x2="53" y2="31" stroke="#fff" stroke-width="3"/>
        <line x1="53" y1="23" x2="57" y2="27" stroke="#fff" stroke-width="3"/>
      </svg>
      <div class="feature-text">RENT ONLINE<br>ANYTIME</div>
    </div>

    <div class="call-band">
      <svg width="1152" height="103" viewBox="0 0 1152 103" aria-hidden="true">
        <rect x="0" y="0" width="1152" height="103" fill="var(--sky)"/>
        <polygon points="88,0 1152,0 1152,103 88,103 40,51.5" fill="var(--navy)"/>
        <g fill="none" stroke="var(--sky)" stroke-width="13" stroke-linejoin="miter">
          <polyline points="100,16 68,51.5 100,87"/>
          <polyline points="140,16 108,51.5 140,87"/>
          <polyline points="180,16 148,51.5 180,87"/>
          <polyline points="220,16 188,51.5 220,87"/>
          <polyline points="260,16 228,51.5 260,87"/>
          <polyline points="300,16 268,51.5 300,87"/>
          <polyline points="340,16 308,51.5 340,87"/>
          <polyline points="380,16 348,51.5 380,87"/>
          <polyline points="420,16 388,51.5 420,87"/>
        </g>
        <g transform="translate(472,16)">
          <path d="M4 4 L14 0 L22 16 L15 22 C18 32 24 40 32 46 L38 40 L52 50 L47 62 C25 60 6 36 4 4 Z" fill="var(--sky)"/>
          <path d="M30 10 A14 14 0 0 1 42 22" fill="none" stroke="var(--sky)" stroke-width="3"/>
          <path d="M30 2 A22 22 0 0 1 50 22" fill="none" stroke="var(--sky)" stroke-width="3"/>
        </g>
      </svg>
      <div class="phone-number">478 555 0142</div>
    </div>
  </div>
</body>
</html>
```